Office Stationary and Business Card package

I need a new fresh looking business card and stationary design. "I need to refresh and update my Stationary and Business card appearance.

We are a family dental practice that handles all phases of dentistry including cosmetic, emergency and implant restoration We like the use of Blue and Grey in the design. i would like to include my website address and Phone numbers on the new project as well as a choice of different back sides to business cards which might include a map, appointment information, or blank depending on the particular card. The business cards should allow for the inclusion of another persons name and title in some location.

Information to be included in stationery:

Gordon T Vallow DMD, FAIDS
A Professional Dental Corporation (this needs to be
somewhere on the stationary and business cards)
48610 Marlow Avenue
Cerritos, CA 90703
PHONE: (562) 471-3095
WEBSITE: www.gordonvallowdmd-example.com

Designs need to be Vibrant, Professional and Clean.
Colors to use: Blue, Grey and White colors.

I currently do not have an existing logo. I would like something simply, similar to the attached.

```html
<!DOCTYPE html>
<html lang="en">
<head>
<meta charset="utf-8">
<title>Vallow Dental – Stationery Set</title>
<link rel="stylesheet" href="https://fonts.googleapis.com/css2?family=Open+Sans:wght@400;600&display=swap">
<style>
  :root {
    --blue: #1f74c4;
    --blue-deep: #1866b0;
    --grey: #4a4b4e;
    --grey-mid: #8a8c90;
    --grey-line: #d5d7da;
    --paper: #ffffff;
    --backdrop: #e8e9eb;
    --ink: #3a3b3d;
    --map-tone: #e6e2d8;
  }
  * { box-sizing: border-box; margin: 0; padding: 0; }
  html, body { width: 1200px; height: 2422px; overflow: hidden; }
  body {
    background: var(--backdrop);
    font-family: "Open Sans", Arial, sans-serif;
    color: var(--ink);
    position: relative;
  }
  .sheet {
    position: absolute;
    background: var(--paper);
    box-shadow: 0 2px 10px rgba(0,0,0,.12);
    overflow: hidden;
  }
  .brand {
    display: flex; align-items: center; gap: 6px;
    color: var(--blue); font-weight: 600; white-space: nowrap;
  }
  .brand-dot { border-radius: 50%; background: var(--blue); flex: none; }
  .footer-band {
    position: absolute; left: 0; right: 0; bottom: 0;
    background: var(--grey);
  }
  .footer-stripes { position: absolute; bottom: 0; }
  .footer-stripes polygon { fill: var(--blue); }

  /* Letterhead */
  .letterhead { left: 70px; top: 90px; width: 500px; height: 707px; }
  .letterhead .brand { position: absolute; left: 36px; top: 40px; font-size: 17px; }
  .letterhead .brand-dot { width: 12px; height: 12px; }
  .letterhead .head-name { position: absolute; right: 40px; top: 50px; font-size: 8px; color: var(--grey); }
  .letterhead .head-rule { position: absolute; left: 160px; right: 40px; top: 64px; height: 2px; background: var(--blue); }
  .letter-body { position: absolute; left: 60px; right: 60px; top: 150px; font-size: 7.5px; line-height: 12px; color: var(--ink); }
  .letter-body p { margin-bottom: 10px; }
  .fee-table { width: 100%; border-collapse: collapse; margin: 6px 0 14px; font-size: 7px; }
  .fee-table th, .fee-table td { text-align: left; padding: 2px 0; border-bottom: 1px solid var(--grey-line); }
  .fee-table th { color: var(--grey); font-weight: 600; border-bottom: 1px solid var(--grey-mid); }
  .fee-table .fee { text-align: right; }
  .letter-sign { margin-top: 14px; font-weight: 600; color: var(--grey); }
  .contact-line {
    position: absolute; font-size: 6px; color: var(--grey-mid);
    display: flex; gap: 12px; white-space: nowrap;
  }
  .letterhead .contact-line { left: 60px; bottom: 24px; }
  .letterhead .footer-band { height: 12px; }

  /* Folder cover */
  .cover { left: 630px; top: 90px; width: 500px; height: 707px; background: var(--blue); display: flex; align-items: center; justify-content: center; }
  .cover .brand { color: var(--paper); font-size: 40px; gap: 14px; }
  .cover .brand-dot { width: 26px; height: 26px; background: var(--paper); }

  /* Compliments slip */
  .slip { left: 70px; top: 870px; width: 500px; height: 236px; }
  .slip .brand { position: absolute; left: 24px; top: 26px; font-size: 15px; }
  .slip .brand-dot { width: 10px; height: 10px; }
  .slip .slip-title { position: absolute; right: 28px; top: 28px; font-size: 11px; color: var(--grey); font-weight: 600; }
  .slip .head-rule { position: absolute; left: 150px; right: 28px; top: 48px; height: 2px; background: var(--blue); }
  .slip .slip-name { position: absolute; left: 24px; top: 66px; font-size: 8px; color: var(--grey); }
  .slip .slip-corp { position: absolute; left: 24px; top: 78px; font-size: 6.5px; color: var(--grey-mid); }
  .slip .contact-line { left: 24px; bottom: 22px; }
  .slip .footer-band { height: 10px; }

  /* Envelope */
  .envelope { left: 630px; top: 870px; width: 500px; height: 236px; }
  .envelope .brand { position: absolute; left: 24px; top: 26px; font-size: 15px; }
  .envelope .brand-dot { width: 10px; height: 10px; }
  .return-address { position: absolute; left: 24px; top: 54px; font-size: 7px; line-height: 10px; color: var(--grey); }
  .envelope .footer-band { height: 26px; }

  /* Business cards */
  .card { left: 200px; width: 800px; height: 457px; }
  .card-front { top: 1190px; }
  .card-back { top: 1720px; }
  .card-front .brand { position: absolute; left: 56px; top: 160px; font-size: 40px; gap: 12px; }
  .card-front .brand-dot { width: 22px; height: 22px; }
  .card-details { position: absolute; left: 440px; top: 90px; }
  .card-name { font-size: 30px; font-weight: 600; color: var(--grey); line-height: 1.1; }
  .card-corp { font-size: 15px; color: var(--blue); margin: 6px 0 26px; }
  .card-lines { list-style: none; font-size: 16px; line-height: 28px; color: var(--ink); }
  .card-lines li { display: flex; align-items: center; gap: 10px; }
  .line-key { width: 18px; color: var(--blue); font-weight: 600; }
  .card-front .footer-band { height: 36px; }
  .card-map { position: absolute; inset: 0; background: linear-gradient(160deg, #ece8df 0%, var(--map-tone) 60%, #dcd8cd 100%); }
</style>
</head>
<body>

<!-- Letterhead -->
<section class="sheet letterhead" aria-label="Letterhead">
  <div class="brand"><span class="brand-dot"></span>Vallow Dental</div>
  <div class="head-name">Gordon T Vallow DMD, FAIDS</div>
  <div class="head-rule"></div>
  <div class="letter-body">
    <p>Thank you for choosing our practice for your family's dental care. This letter confirms your treatment plan and the visits we discussed. Please review the items below and call our front desk with any questions before your next appointment.</p>
    <p>Each phase of care is listed with its estimated fee. Insurance benefits will be applied at the time of service, and any balance may be arranged in monthly payments.</p>
    <table class="fee-table">
      <tr><th>Treatment</th><th class="fee">Fee</th></tr>
      <tr><td>Exam and cleaning</td><td class="fee">$120</td></tr>
      <tr><td>Digital x-rays</td><td class="fee">$85</td></tr>
      <tr><td>Composite filling</td><td class="fee">$160</td></tr>
      <tr><td>Implant consultation</td><td class="fee">$0</td></tr>
      <tr><td>Whitening tray</td><td class="fee">$240</td></tr>
    </table>
    <p>We look forward to seeing you soon.</p>
    <p>Kind regards,</p>
    <p class="letter-sign">Gordon T Vallow DMD, FAIDS</p>
  </div>
  <div class="contact-line">
    <span>48610 Marlow Avenue, Cerritos, CA 90703</span>
    <span>(562) 471-3095</span>
    <span>www.gordonvallowdmd-example.com</span>
  </div>
  <div class="footer-band"></div>
  <svg class="footer-stripes" style="right:40px" width="46" height="22" viewBox="0 0 46 22" aria-hidden="true">
    <polygon points="12,0 22,0 10,22 0,22"/><polygon points="30,0 40,0 28,22 18,22"/>
  </svg>
</section>

<!-- Folder cover -->
<section class="sheet cover" aria-label="Presentation folder cover">
  <div class="brand"><span class="brand-dot"></span>Vallow Dental</div>
</section>

<!-- Compliments slip -->
<section class="sheet slip" aria-label="Compliments slip">
  <div class="brand"><span class="brand-dot"></span>Vallow Dental</div>
  <div class="slip-title">With Compliments</div>
  <div class="head-rule"></div>
  <div class="slip-name">Gordon T Vallow DMD, FAIDS</div>
  <div class="slip-corp">A Professional Dental Corporation</div>
  <div class="contact-line">
    <span>48610 Marlow Avenue, Cerritos, CA 90703</span>
    <span>(562) 471-3095</span>
    <span>www.gordonvallowdmd-example.com</span>
  </div>
  <div class="footer-band"></div>
  <svg class="footer-stripes" style="right:30px" width="40" height="20" viewBox="0 0 40 20" aria-hidden="true">
    <polygon points="10,0 19,0 9,20 0,20"/><polygon points="26,0 35,0 25,20 16,20"/>
  </svg>
</section>

<!-- Envelope -->
<section class="sheet envelope" aria-label="Envelope">
  <div class="brand"><span class="brand-dot"></span>Vallow Dental</div>
  <div class="return-address">
    Gordon T Vallow DMD, FAIDS<br>
    48610 Marlow Avenue<br>
    Cerritos, CA 90703
  </div>
  <div class="footer-band"></div>
  <svg class="footer-stripes" style="right:30px" width="50" height="36" viewBox="0 0 50 36" aria-hidden="true">
    <polygon points="14,0 25,0 11,36 0,36"/><polygon points="34,0 45,0 31,36 20,36"/>
  </svg>
</section>

<!-- Business card, front -->
<section class="sheet card card-front" aria-label="Business card front">
  <div class="brand"><span class="brand-dot"></span>Vallow Dental</div>
  <div class="card-details">
    <div class="card-name">Gordon T Vallow DMD, FAIDS</div>
    <div class="card-corp">A Professional Dental Corporation</div>
    <ul class="card-lines">
      <li><span class="line-key">A.</span>48610 Marlow Avenue</li>
      <li><span class="line-key"></span>Cerritos, CA 90703</li>
      <li><span class="line-key">P.</span>(562) 471-3095</li>
      <li><span class="line-key">W.</span>www.gordonvallowdmd-example.com</li>
    </ul>
  </div>
  <div class="footer-band"></div>
  <svg class="footer-stripes" style="right:50px" width="80" height="56" viewBox="0 0 80 56" aria-hidden="true">
    <polygon points="22,0 40,0 18,56 0,56"/><polygon points="54,0 72,0 50,56 32,56"/>
  </svg>
</section>

<!-- Business card, back -->
<section class="sheet card card-back" aria-label="Business card back">
  <div class="card-map" role="img" aria-label="Street map showing the practice location"></div>
</section>

</body>
</html>
```